Buchcover-Design für psychologischen Ratgeber Morgens voller Mut!
Zielgruppe
Veröffentlichung psychologischer Ratgeber. Zielgruppe sind Erwachsene.
Aufgabenstellung
keine besondere Vorgaben, ein eyecatching-Cover wäre super. Der Titel des Buches lautet: Morgens voller Mut! Der Untertitel lautet: Heitere Seelenkunde für stille Kraft und Zuversicht
Autoren: Dr. Hanna Wiesmoor-Kalbach, Dr. Lukas Kalbach
Vielleicht macht es Sinn, einen Button mit: 199 Praxistipps auf dem Cover anzuführen.
Das Buch wird als Softcover und Ebook auf lesewelt veröffentlicht. Das Format ist 6 mal 9 Zoll und hat 425 Seiten.

```html
<!DOCTYPE html>
<html lang="de">
<head>
<meta charset="utf-8">
<title>Morgens voller Mut! – Buchcover</title>
<link href="https://fonts.googleapis.com/css2?family=Anton&family=Jost:wght@400;500;700&display=swap" rel="stylesheet">
<style>
  :root {
    --olive: #bcc40f;
    --pink: #e5007e;
    --ink: #1e1e1c;
  }
  html, body {
    margin: 0;
    padding: 0;
    overflow: hidden;
    background: var(--olive);
  }
  .cover {
    position: relative;
    width: 828px;
    height: 1200px;
    overflow: hidden;
    background: var(--olive);
    color: var(--ink);
    font-family: "Jost", "Futura", sans-serif;
  }
  .authors {
    position: absolute;
    top: 34px;
    left: 0;
    width: 100%;
    margin: 0;
    text-align: center;
    font-size: 20px;
    letter-spacing: 0.3px;
  }
  .authors .sep {
    display: inline-block;
    width: 7px;
    height: 7px;
    border-radius: 50%;
    background: var(--ink);
    margin: 0 12px;
    vertical-align: middle;
  }
  .title-art {
    position: absolute;
    top: 0;
    left: 0;
    width: 828px;
    height: 1200px;
  }
  .title-small {
    font-family: "Jost", sans-serif;
    font-weight: 400;
    fill: var(--ink);
  }
  .title-big {
    font-family: "Anton", "Impact", sans-serif;
    fill: var(--pink);
  }
  .badge {
    font-family: "Jost", sans-serif;
    font-weight: 500;
    fill: var(--ink);
  }
  .subtitle {
    position: absolute;
    top: 880px;
    left: 0;
    width: 100%;
    margin: 0;
    text-align: center;
    font-size: 31px;
    letter-spacing: 0.2px;
  }
  .publisher {
    position: absolute;
    top: 1128px;
    left: 0;
    width: 100%;
    margin: 0;
    text-align: center;
    font-size: 30px;
    font-weight: 700;
  }
</style>
</head>
<body>
<main class="cover">
  <p class="authors">Dr. Hanna Wiesmoor-Kalbach<span class="sep"></span>Dr. Lukas Kalbach</p>

  <svg class="title-art" viewBox="0 0 828 1200" aria-label="Morgens voller Mut!">
    <text class="title-small" x="85" y="311" font-size="90" textLength="500" lengthAdjust="spacingAndGlyphs">MORGENS</text>
    <text class="title-big" x="-6" y="552" font-size="266" textLength="840" lengthAdjust="spacingAndGlyphs">VOLLER</text>
    <text class="title-big" x="-6" y="882" font-size="370" textLength="840" lengthAdjust="spacingAndGlyphs">MUT!</text>
    <rect x="100" y="574" width="92" height="210" fill="var(--olive)"/>
    <g transform="translate(143 776) rotate(-90)">
      <text class="badge" x="0" y="0" font-size="38">mit 199</text>
      <text class="badge" x="0" y="40" font-size="38" font-weight="700">Praxistipps</text>
    </g>
  </svg>

  <p class="subtitle">Heitere Seelenkunde für stille Kraft und Zuversicht</p>
  <p class="publisher">Verlag Lichtung</p>
</main>
</body>
</html>
```